Social Media Graphics - ALL TEXT RK

We are looking for a series of social media graphics for Instagram (standard size 1:1 (1080x1080px) that are ALL TEXT. We want the following quotes below on each graphic; one quote per graphic. AND, In very small letters at the bottom of each graphic, add @RKMarlowLive

The look and feel of these graphics should be complimentary to the color palette attached below; but keep them simple. But the design is up to you; at the end of this document, I provided various samples of all text graphics that I like as examples.

Target Market(s)

women looking to lose weight

Industry/Entity Type

health and wellness

Colors
E54698
E96AAD
F1A4CE
F9D9EA
FCEFF6

Requirements
Must have
• the quotes in the document
Should not have
• no stock photography

```html
<!DOCTYPE html>
<html lang="en">
<head>
<meta charset="utf-8">
<title>RK Social Graphics – All Text Series</title>
<link rel="stylesheet" href="https://fonts.googleapis.com/css2?family=Poppins:wght@300;400;800&display=swap">
<style>
  :root {
    --canvas: #b9b9b9;
    --pink-deep: #e54698;
    --pink-mid: #e96aad;
    --pink-soft: #f1a4ce;
    --white: #ffffff;
  }
  * { margin: 0; padding: 0; box-sizing: border-box; }
  html, body { width: 1200px; height: 809px; overflow: hidden; background: var(--canvas); }
  body { position: relative; font-family: "Poppins", Arial, sans-serif; color: var(--white); }

  .post {
    position: absolute;
    width: 340px; height: 340px;
    overflow: hidden;
    background: linear-gradient(180deg, var(--pink-deep) 0%, #e75aa5 60%, var(--pink-mid) 100%);
    box-shadow: 0 2px 6px rgba(0,0,0,0.12);
  }
  .post--wake { left: 55px; top: 46px; background: radial-gradient(circle at 50% 45%, var(--pink-mid) 0%, var(--pink-deep) 75%); }
  .post--struggle { left: 430px; top: 46px; }
  .post--supplement { left: 805px; top: 46px; }
  .post--finally { left: 55px; top: 423px; }
  .post--hormones { left: 430px; top: 423px; }

  .post__decor { position: absolute; inset: 0; width: 340px; height: 340px; }

  .post__frame {
    position: absolute; left: 8px; top: 8px; right: 8px; bottom: 8px;
    border: 1px solid var(--white);
  }

  .quote {
    position: absolute; left: 0; right: 0;
    text-transform: uppercase;
  }
  .quote b { font-weight: 800; }
  .quote--wake {
    top: 34px; text-align: center;
    font-size: 32px; line-height: 36.6px; font-weight: 300;
    letter-spacing: -0.2px;
  }
  .quote--struggle {
    top: 40px; left: 36px; right: 10px; text-align: left;
    font-size: 25px; line-height: 36.6px; font-weight: 300;
  }
  .quote--supplement {
    top: 40px; text-align: center;
    font-size: 25px; line-height: 36.6px; font-weight: 300;
  }
  .quote--finally {
    top: 48px; text-align: center;
    font-size: 27px; line-height: 36.6px; font-weight: 300;
  }
  .quote--hormones {
    top: 47px; left: 10px; right: 35px; text-align: right;
    font-size: 27px; line-height: 36.6px; font-weight: 800;
  }

  .handle {
    position: absolute; left: 0; right: 0;
    text-align: center;
    font-size: 10px; font-weight: 400;
  }
  .post--wake .handle { top: 306px; }
  .post--struggle .handle, .post--supplement .handle { top: 309px; }
  .post--finally .handle, .post--hormones .handle { top: 302px; }
</style>
</head>
<body>

  <section class="post post--wake">
    <div class="post__frame"></div>
    <p class="quote quote--wake">
      <b>Wake up<br>tomorrow<br>witha flatter<br>belly- yes,</b> this<br>overnight<br>remedy works<br>like magic!
    </p>
    <p class="handle">@RKMarlowLive</p>
  </section>

  <section class="post post--struggle">
    <svg class="post__decor" viewBox="0 0 340 340" aria-hidden="true">
      <g stroke="#f1a4ce" stroke-opacity="0.45" stroke-width="0.6" fill="none">
        <line x1="113" y1="0" x2="0" y2="113"/>
        <line x1="228" y1="0" x2="340" y2="112"/>
        <line x1="0" y1="228" x2="112" y2="340"/>
        <line x1="340" y1="228" x2="228" y2="340"/>
      </g>
    </svg>
    <p class="quote quote--struggle">
      Struggling with<br>bloating and belly<br>fat? <b>Try this<br>natural<br>solutiontonight,<br>and wake up<br>feeling lighter!</b>
    </p>
    <p class="handle">@RKMarlowLive</p>
  </section>

  <section class="post post--supplement">
    <svg class="post__decor" viewBox="0 0 340 340" aria-hidden="true">
      <g stroke="#f1a4ce" stroke-opacity="0.45" stroke-width="0.6" fill="none">
        <polyline points="100,0 0,120 18,168"/>
        <line x1="100" y1="0" x2="340" y2="240"/>
        <line x1="340" y1="160" x2="160" y2="340"/>
        <line x1="0" y1="150" x2="18" y2="168"/>
      </g>
    </svg>
    <p class="quote quote--supplement">
      One supplement,<br>one night; your<br>belly bloat could<br>be gone by<br>morning.<br><b>Here's how it<br>works!</b>
    </p>
    <p class="handle">@RKMarlowLive</p>
  </section>

  <section class="post post--finally">
    <svg class="post__decor" viewBox="0 0 340 340" aria-hidden="true">
      <defs>
        <linearGradient id="finally-disc" x1="0" y1="0" x2="0" y2="1">
          <stop offset="0" stop-color="#e96aad"/>
          <stop offset="0.45" stop-color="#e75aa5"/>
          <stop offset="1" stop-color="#e54698"/>
        </linearGradient>
      </defs>
      <circle cx="170" cy="170" r="170" fill="url(#finally-disc)"/>
    </svg>
    <p class="quote quote--finally">
      Finally-a<br>natural solution<br>that flattens<br>your belly and<br>eases stomach<br>bloat
    </p>
    <p class="handle">@RKMarlowLive</p>
  </section>

  <section class="post post--hormones">
    <svg class="post__decor" viewBox="0 0 340 340" aria-hidden="true">
      <g stroke="#f1a4ce" stroke-opacity="0.45" stroke-width="0.6" fill="none">
        <line x1="230" y1="0" x2="340" y2="110"/>
        <line x1="0" y1="228" x2="112" y2="340"/>
        <line x1="340" y1="228" x2="228" y2="340"/>
      </g>
      <path d="M0,0 H128 A170,170 0 0 1 0,132 Z" fill="#e54698" opacity="0.9"/>
      <path d="M70,340 A100,100 0 0 1 270,340 Z" fill="#e54698"/>
    </svg>
    <p class="quote quote--hormones">
      Sis, your<br>hormones are<br>out of whack -<br>that's why the<br>weight won't<br>budge!
    </p>
    <p class="handle">@RKMarlowLive</p>
  </section>

</body>
</html>
```